International business needs business cards

Our company, DOR Ventures Inc. is in the business of supplying a range construction products with particular emphasis on CEMENT. We have developed our own brand - BRUNVALE MATERIALS - with which to infiltrate the market. We are launching our brand of cement (BRUNVALE Type IS Cement) into the Caribbean which is unlike anything this market has ever seen. A monopoly has existed here for the past 60-odd years and the market has now opened to allow the importation of other brands and consumers are anxious and ready for change/improvement. We are very excited to be launching and want to make a great first impression. We will be conducting workshops and seminars (from government level to the hardware store owners) and we want our business card to give us the strong, confident introduction that we need.

Target Market(s)

construction; builders; engineers; home owners

Industry/Entity Type

Construction

Contact Information for Business Card

Marisol Penwick
CEO
cell # 1 555 4817730
Ground floor,Lantern Plaza Suite 2483
George Town,Grand Cayman
Cayman Islands,KY1-2250
EMAIL: m.penwick@dorventuresinc.example
web site dorventuresinc.example

COMPANY: skype info dor.ventures.example

second card
Tamsin Rowe-Penwick
CFO
CELL# 1 555 604 3917
George Town,Grand Cayman
Cayman Islands,KY1-2250
EMAIL: t.rowepenwick@dorventuresinc.example
website dorventuresinc.example

Requirements
Must have
• Business cards must display BOTH logos - DOR is the company and BRUNVALE is the brand.

```html
<!DOCTYPE html>
<html lang="en">
<head>
<meta charset="utf-8">
<title>DOR Ventures Inc. – Business Card</title>
<link rel="stylesheet" href="https://fonts.googleapis.com/css2?family=Open+Sans:wght@400;600;700;800&display=swap">
<style>
  :root {
    --backdrop: #2b2b2b;
    --card: #ffffff;
    --ink: #111111;
    --ink-soft: #3a3a3a;
    --mark-grey: #4a4a4a;
    --accent: #8e1b1f;
    --card-shadow: rgba(0,0,0,0.45);
  }
  * { margin: 0; padding: 0; box-sizing: border-box; }
  html, body {
    width: 1200px; height: 900px; overflow: hidden;
    background: var(--backdrop);
    font-family: "Open Sans", Arial, sans-serif;
  }
  .canvas { position: relative; width: 1200px; height: 900px; }
  .card {
    position: absolute; left: 260px;
    width: 680px; height: 390px;
    background: var(--card);
    border-radius: 26px;
    box-shadow: 0 14px 30px var(--card-shadow);
    overflow: hidden;
  }
  .card--back { top: 45px; }
  .card--front { top: 465px; }

  /* back side */
  .brand-mark {
    position: absolute; left: 0; right: 0; top: 140px;
    display: flex; align-items: center; justify-content: center; gap: 14px;
  }
  .brand-mark__dot {
    width: 34px; height: 34px; border-radius: 50%; background: var(--mark-grey);
  }
  .brand-mark__name {
    font-size: 44px; font-weight: 700; letter-spacing: 4px; color: var(--mark-grey);
  }
  .brand-handle {
    position: absolute; left: 0; right: 0; top: 318px;
    display: flex; align-items: center; justify-content: center; gap: 8px;
    font-size: 17px; font-weight: 600; color: var(--ink);
  }
  .brand-handle__dot {
    width: 14px; height: 14px; border-radius: 50%; background: var(--accent);
  }

  /* front side */
  .company {
    position: absolute; left: 50px; top: 52px;
    display: flex; align-items: center; gap: 16px;
  }
  .company__square { width: 70px; height: 70px; background: var(--accent); }
  .company__name { font-size: 34px; font-weight: 800; color: var(--ink); }
  .person { position: absolute; left: 50px; top: 150px; }
  .person__name {
    font-size: 28px; font-weight: 800; color: var(--ink); letter-spacing: 0.5px;
    text-transform: uppercase;
  }
  .person__role { font-size: 17px; font-weight: 600; color: var(--accent); margin-top: 2px; }
  .address {
    position: absolute; left: 50px; top: 230px;
    font-size: 16px; font-weight: 600; color: var(--ink-soft); line-height: 1.3;
  }
  .contacts {
    position: absolute; left: 50px; top: 295px; list-style: none;
    font-size: 16px; font-weight: 600; color: var(--ink-soft); line-height: 1.3;
  }
  .contacts li { display: flex; align-items: center; gap: 8px; }
  .contacts svg { width: 13px; height: 13px; fill: var(--accent); flex: none; }
</style>
</head>
<body>
<main class="canvas">
  <section class="card card--back" aria-label="Card back">
    <div class="brand-mark">
      <span class="brand-mark__dot"></span>
      <span class="brand-mark__name">BRUNVALE</span>
    </div>
    <div class="brand-handle">
      <span class="brand-handle__dot"></span>
      <span>dor.ventures.example</span>
    </div>
  </section>

  <section class="card card--front" aria-label="Card front">
    <div class="company">
      <span class="company__square"></span>
      <span class="company__name">DOR Ventures Inc.</span>
    </div>
    <div class="person">
      <h1 class="person__name">Marisol Penwick</h1>
      <p class="person__role">CEO</p>
    </div>
    <address class="address" style="font-style:normal">
      Ground floor,Lantern Plaza Suite 2483<br>
      George Town,Grand Cayman<br>
      Cayman Islands,KY1-2250
    </address>
    <ul class="contacts">
      <li>
        <svg viewBox="0 0 16 16" aria-hidden="true"><path d="M3 1l3 1 1 3-2 2c1 2 2 3 4 4l2-2 3 1 1 3-2 2C7 15 1 9 1 3z"/></svg>
        1 555 4817730
      </li>
      <li>
        <svg viewBox="0 0 16 16" aria-hidden="true"><path d="M1 3h14v10H1z M2 4l6 5 6-5" fill="none" stroke="#8e1b1f" stroke-width="1.6"/></svg>
        m.penwick@dorventuresinc.example
      </li>
      <li>
        <svg viewBox="0 0 16 16" aria-hidden="true"><circle cx="8" cy="8" r="7"/><path d="M1 8h14M8 1c-3 4-3 10 0 14M8 1c3 4 3 10 0 14" stroke="#fff" stroke-width="1" fill="none"/></svg>
        www.dorventuresinc.example
      </li>
    </ul>
  </section>
</main>
</body>
</html>
```